Updated Business Card for Optometry Practice

We're a growing optometry practice that is moving to a beautiful new office and we want to update our business card. We just updated our logo so the new card should reflect the new logo. Our practice continually invests in state of the art instruments to help us provide eye care that is thorough, comfortable, efficient and educational.

I've attached our current card and logo. You can reference this for the information I would like on the card. The tag line on the back is "We're changing the way you see."

Upon completion of this project we will need (amongst other formats) Photoshop files of the card so I can change employee names to print cards for each employee.

```html
<!DOCTYPE html>
<html lang="en">
<head>
<meta charset="utf-8">
<title>Brightwater Family Eyecare – Business Card</title>
<link rel="stylesheet" href="https://fonts.googleapis.com/css2?family=Lato:wght@400;700&family=Montserrat:wght@500&family=Great+Vibes&display=swap">
<style>
  :root {
    --navy: #13284b;
    --navy-soft: #17305a;
    --gold: #d9ad2b;
    --white: #ffffff;
    --backdrop: #9a9a9a;
  }
  * { box-sizing: border-box; margin: 0; padding: 0; }
  html, body { width: 1200px; height: 1015px; overflow: hidden; }
  body {
    background: var(--backdrop);
    position: relative;
    font-family: "Lato", sans-serif;
  }
  .card {
    position: absolute;
    width: 560px;
    height: 320px;
    background: var(--navy);
    box-shadow: 0 10px 24px rgba(0,0,0,.35);
    color: var(--white);
  }
  .card--front { left: 60px; top: 110px; }
  .card--back { left: 580px; top: 575px; }

  /* Front */
  .brand {
    position: absolute;
    left: 0; right: 0; top: 92px;
    display: flex; align-items: center; justify-content: center; gap: 14px;
  }
  .brand__dot {
    width: 26px; height: 26px; border-radius: 50%;
    background: var(--gold);
  }
  .brand__name {
    font-family: "Montserrat", sans-serif;
    font-weight: 500;
    font-size: 30px;
    letter-spacing: 3px;
    color: var(--white);
    line-height: 1.15;
    text-transform: uppercase;
  }
  .tagline {
    position: absolute;
    left: 0; right: 0; top: 205px;
    text-align: center;
    font-family: "Great Vibes", cursive;
    font-size: 40px;
    color: var(--gold);
  }

  /* Back */
  .contact {
    position: absolute;
    inset: 0;
    display: flex; flex-direction: column; align-items: center; justify-content: center;
    text-align: center;
  }
  .contact__name {
    font-weight: 700; font-size: 24px; color: var(--gold); letter-spacing: .5px;
  }
  .contact__role { font-size: 16px; margin-top: 2px; }
  .contact__icons {
    display: flex; align-items: center; gap: 6px; margin: 10px 0;
  }
  .contact__rule { width: 60px; height: 1px; background: var(--gold); }
  .contact__icon {
    width: 22px; height: 22px; border-radius: 50%; background: var(--gold);
    display: flex; align-items: center; justify-content: center;
  }
  .contact__line { font-size: 15px; line-height: 1.35; }
  .contact__divider { width: 170px; height: 1px; background: var(--gold); margin: 10px 0 8px; }
  .contact__practice { font-size: 16px; color: var(--gold); }
  .contact__address { font-size: 15px; line-height: 1.35; }
</style>
</head>
<body>

<section class="card card--front" aria-label="Card front">
  <div class="brand">
    <span class="brand__dot"></span>
    <span class="brand__name">Brightwater<br>Family Eyecare</span>
  </div>
  <p class="tagline">We're changing the way you see</p>
</section>

<section class="card card--back" aria-label="Card back">
  <div class="contact">
    <p class="contact__name">DANIEL MERCER, OD</p>
    <p class="contact__role">Optometrist</p>
    <div class="contact__icons">
      <span class="contact__rule"></span>
      <span class="contact__icon" aria-label="Phone">
        <svg width="12" height="12" viewBox="0 0 24 24"><path d="M6.6 10.8a15 15 0 0 0 6.6 6.6l2.2-2.2c.3-.3.7-.4 1-.2 1.1.4 2.3.6 3.6.6.6 0 1 .4 1 1V20c0 .6-.4 1-1 1A17 17 0 0 1 3 4c0-.6.4-1 1-1h3.5c.6 0 1 .4 1 1 0 1.3.2 2.5.6 3.6.1.3 0 .7-.2 1z" fill="#13284b"/></svg>
      </span>
      <span class="contact__icon" aria-label="Email">
        <svg width="12" height="12" viewBox="0 0 24 24"><rect x="2" y="5" width="20" height="14" fill="#13284b"/><path d="M2 5l10 8 10-8" stroke="#d9ad2b" stroke-width="2" fill="none"/></svg>
      </span>
      <span class="contact__icon" aria-label="Website">
        <svg width="12" height="12" viewBox="0 0 24 24" fill="none" stroke="#13284b" stroke-width="2"><circle cx="12" cy="12" r="9"/><path d="M3 12h18M12 3c3 3 3 15 0 18M12 3c-3 3-3 15 0 18"/></svg>
      </span>
      <span class="contact__rule"></span>
    </div>
    <p class="contact__line">(555) 014-2290</p>
    <p class="contact__line">dan@brightwatereyecare.com</p>
    <p class="contact__line">www.brightwatereyecare.com</p>
    <span class="contact__divider"></span>
    <p class="contact__practice">Brightwater Family Eyecare</p>
    <p class="contact__address">2780 Harlow Ridge Blvd #210<br>Brightwater, MO 63000</p>
  </div>
</section>

</body>
</html>
```